Building company business card

Design and print business cards for BRENTHOLM PTY LTD.
A residantial homes building company.
Mark Lantern already designed the company Logo.

```html
<!DOCTYPE html>
<html lang="en">
<head>
<meta charset="utf-8">
<title>BRENTHOLM PTY LTD – Business Card</title>
<link href="https://fonts.googleapis.com/css2?family=Montserrat:wght@500;600;800&display=swap" rel="stylesheet">
<style>
  :root {
    --navy: #0f1f6b;
    --gold: #d4a446;
    --gold-light: #e9c46a;
    --white: #ffffff;
    --backdrop: #3b3b3b;
  }
  * { box-sizing: border-box; margin: 0; padding: 0; }
  html, body {
    width: 1200px; height: 1200px; overflow: hidden;
    background: var(--backdrop);
    font-family: "Montserrat", sans-serif;
  }
  .sheet {
    position: relative; width: 1200px; height: 1200px;
    display: flex; flex-direction: column; align-items: center;
    justify-content: center; gap: 58px;
  }
  .card {
    position: relative; width: 860px; height: 491px;
    border-radius: 34px; overflow: hidden;
    box-shadow: 0 18px 40px rgba(0,0,0,.35);
  }
  .card--front { background: var(--white); }
  .card--back { background: var(--navy); }
  .card__shape { position: absolute; inset: 0; width: 100%; height: 100%; }

  .contact {
    position: absolute; left: 64px; top: 150px; color: var(--white);
  }
  .contact__name {
    color: var(--gold); font-weight: 600; font-size: 27px; letter-spacing: .5px;
  }
  .contact__role {
    font-weight: 500; font-size: 15px; letter-spacing: 1px; margin: 2px 0 22px 14px;
  }
  .contact__list { list-style: none; margin-left: 14px; }
  .contact__item {
    display: flex; align-items: flex-start; gap: 12px;
    font-size: 17px; font-weight: 500; line-height: 1.3; margin-bottom: 6px;
  }
  .contact__icon { width: 20px; height: 20px; flex: none; margin-top: 2px; }
  .contact__reg {
    margin: 20px 0 0 46px; font-size: 16px; font-weight: 500; line-height: 1.3;
  }

  .brand {
    position: absolute; display: flex; align-items: center; gap: 14px;
  }
  .brand__mark { background: var(--gold); flex: none; }
  .brand__name { font-weight: 800; letter-spacing: 1px; }
  .card--front .brand { left: 590px; top: 220px; }
  .card--front .brand__mark { width: 22px; height: 22px; }
  .card--front .brand__name { color: var(--navy); font-size: 30px; }
  .card--back .brand { left: 50%; top: 50%; transform: translate(-50%, -50%); gap: 22px; }
  .card--back .brand__mark { width: 44px; height: 44px; }
  .card--back .brand__name { color: var(--white); font-size: 62px; }
</style>
</head>
<body>
<main class="sheet">
  <section class="card card--front" aria-label="Business card front">
    <svg class="card__shape" viewBox="0 0 860 491" preserveAspectRatio="none" aria-hidden="true">
      <polygon points="0,0 430,0 505,150 545,491 0,491" fill="var(--navy)"/>
      <polyline points="444,0 519,150 559,491" fill="none" stroke="var(--gold)" stroke-width="6"/>
    </svg>
    <div class="contact">
      <p class="contact__name">THEODORE (TED) MARLOWE</p>
      <p class="contact__role">DIRECTOR</p>
      <ul class="contact__list">
        <li class="contact__item">
          <svg class="contact__icon" viewBox="0 0 24 24"><path fill="var(--gold)" d="M6.6 10.8a15 15 0 0 0 6.6 6.6l2.2-2.2c.3-.3.7-.4 1-.2 1.1.4 2.3.6 3.6.6.6 0 1 .4 1 1V20c0 .6-.4 1-1 1A17 17 0 0 1 3 4c0-.6.4-1 1-1h3.5c.6 0 1 .4 1 1 0 1.3.2 2.5.6 3.6.1.3 0 .7-.2 1z"/></svg>
          <span>0400 555 128</span>
        </li>
        <li class="contact__item">
          <svg class="contact__icon" viewBox="0 0 24 24"><rect x="2" y="5" width="20" height="14" rx="1" fill="var(--gold)"/><path d="M2 6l10 7 10-7" fill="none" stroke="var(--navy)" stroke-width="1.6"/></svg>
          <span>tm@brentholm-pl.com</span>
        </li>
        <li class="contact__item">
          <svg class="contact__icon" viewBox="0 0 24 24"><path fill="var(--gold)" d="M12 2a7 7 0 0 0-7 7c0 5 7 13 7 13s7-8 7-13a7 7 0 0 0-7-7zm0 9.5A2.5 2.5 0 1 1 12 6.5a2.5 2.5 0 0 1 0 5z"/></svg>
          <span>BRENTHOLM PTY LTD<br>PO Box 482 Elmridge Vic 3999</span>
        </li>
      </ul>
      <p class="contact__reg">ABN- 51 824 753 556<br>CDB-U 48215</p>
    </div>
    <div class="brand">
      <span class="brand__mark"></span>
      <span class="brand__name">BRENTHOLM</span>
    </div>
  </section>

  <section class="card card--back" aria-label="Business card back">
    <div class="brand">
      <span class="brand__mark"></span>
      <span class="brand__name">BRENTHOLM</span>
    </div>
  </section>
</main>
</body>
</html>
```